Stage Show Poster - The Harbour of Lanterns.

We are looking for an eye catching A3 poster to advertise our upcoming production ‘The Harbour of Lanterns’. Please see the two attached files for all the information about the show and what we need on the poster.
The Synopsis file is provided to give you an idea of the production its not ment to be on the poster.

Target Market(s)

General Public western english speaking

Requirements
Must have
• See Poster Requirements File. A3 Portrait Poster.
Should not have
• Pictures of any prevous casts from the show or film.

```html
<!DOCTYPE html>
<html lang="en">
<head>
<meta charset="utf-8">
<title>The Harbour of Lanterns – Poster</title>
<link href="https://fonts.googleapis.com/css2?family=Great+Vibes&family=Open+Sans:ital,wght@1,400;1,700&family=Roboto+Condensed:wght@400;700&display=swap" rel="stylesheet">
<style>
  :root {
    --ink: #4a4540;
    --body-text: #4d4a4a;
    --sky-dark: #6e6a6c;
    --sky-gold: #f6d98f;
    --sky-glow: #fdf0c4;
    --haze: #e9d6dc;
    --hills: #d7b9c4;
    --footer-bg: #ffffff;
    --booking-bg: #0c1526;
    --booking-edge: #5a7fc4;
    --booking-text: #ffffff;
    --strip: #9a7a60;
  }
  * { margin: 0; padding: 0; box-sizing: border-box; }
  html, body { width: 848px; height: 1200px; overflow: hidden; background: #fff; }
  .poster { position: relative; width: 848px; height: 1200px; overflow: hidden; }

  .sky-scene {
    position: absolute; inset: 0;
    background:
      radial-gradient(ellipse 420px 260px at 330px 460px, rgba(253,240,196,0.95), rgba(253,240,196,0) 70%),
      radial-gradient(ellipse 600px 180px at 420px 60px, rgba(95,90,96,0.95), rgba(95,90,96,0) 75%),
      radial-gradient(ellipse 260px 200px at 760px 260px, rgba(120,110,112,0.7), rgba(120,110,112,0) 75%),
      linear-gradient(180deg, var(--sky-dark) 0%, #b9a28a 14%, var(--sky-gold) 30%, var(--sky-glow) 48%, #f3e6cf 62%, var(--haze) 76%, var(--hills) 100%);
  }
  .hills {
    position: absolute; left: 0; top: 800px; width: 848px; height: 280px;
    background: linear-gradient(180deg, rgba(215,185,196,0) 0%, rgba(205,170,180,0.55) 45%, rgba(190,150,160,0.7) 100%);
  }

  .title {
    position: absolute; left: 0; width: 848px;
    font-family: "Great Vibes", cursive;
    color: var(--ink);
    font-weight: 400;
    line-height: 1;
  }
  .title-line-1 { top: 205px; font-size: 130px; text-align: center; padding-right: 20px; }
  .title-line-2 { top: 355px; font-size: 130px; text-align: center; padding-left: 70px; }

  .show-details {
    position: absolute; top: 570px; left: 0; width: 848px;
    text-align: center;
    font-family: "Open Sans", sans-serif; font-style: italic;
    font-size: 23px; color: var(--body-text);
  }
  .show-details p { height: 48.5px; line-height: 36px; }

  .credits {
    position: absolute; top: 970px; left: 0; width: 848px;
    text-align: center;
    font-family: "Open Sans", sans-serif; font-style: italic;
    font-size: 14px; color: #222; line-height: 30px;
  }

  .footer {
    position: absolute; left: 0; top: 1078px; width: 848px; height: 78px;
    background: var(--footer-bg);
  }
  .company-name {
    position: absolute; left: 24px; top: 26px;
    display: flex; align-items: center; gap: 8px;
    font-family: "Open Sans", sans-serif; font-style: italic; font-weight: 700;
    font-size: 14px; color: #5a2a78;
  }
  .company-name .mark { width: 14px; height: 14px; background: #5a2a78; }
  .licence-note {
    position: absolute; left: 163px; top: 24px;
    font-family: "Open Sans", sans-serif; font-style: italic;
    font-size: 10px; line-height: 15px; color: #222;
  }
  .booking-box {
    position: absolute; left: 455px; top: 15px; width: 358px; height: 53px;
    background: var(--booking-bg);
    border-bottom: 4px solid var(--booking-edge);
    text-align: center; color: var(--booking-text);
    font-family: "Roboto Condensed", sans-serif;
  }
  .booking-box .url { font-size: 23px; line-height: 28px; padding-top: 2px; }
  .booking-box .label { font-size: 12px; font-weight: 700; line-height: 14px; }

  .scene-strip {
    position: absolute; left: 0; top: 1156px; width: 848px; height: 44px;
    background: linear-gradient(180deg, #b99a86, var(--strip) 60%, #7d6250);
  }
</style>
</head>
<body>
<div class="poster">
  <div class="sky-scene" role="img" aria-label="Painted sky with golden light breaking through grey clouds over misty hills"></div>
  <div class="hills" role="img" aria-label="Soft pink and lavender mountain range in haze"></div>

  <h1 class="title">
    <span class="title title-line-1">The Harbour</span>
    <span class="title title-line-2">of Lanterns</span>
  </h1>

  <div class="show-details">
    <p>Bramholt Town Hall</p>
    <p>7:30pm on the 15th to 16th November;</p>
    <p>2:30 pm &amp; 7:30pm on the 17th November 2012</p>
    <p>www.bramholtboxoffice.co.uk</p>
  </div>

  <div class="credits">
    <p>Music by EDWIN MARLOWE &nbsp; Lyrics by FELIX ASHDOWN</p>
    <p>Book by ARTHUR WHITCOMBE and LEONARD HALE</p>
    <p>Suggested by "The Lantern Keepers" by Elsa Marit Voss.</p>
  </div>

  <footer class="footer">
    <div class="company-name"><span class="mark"></span>Kestrel Players</div>
    <p class="licence-note">This amateur production is presented<br>by arrangement with HALDEN LICENSING LTD.<br>on behalf of Crane &amp; Lowe Theatricals of New York.</p>
    <div class="booking-box">
      <div class="url">www.bramholtboxoffice.co.uk</div>
      <div class="label">Online Booking</div>
    </div>
  </footer>

  <div class="scene-strip" role="img" aria-label="Strip of painted landscape in warm browns"></div>
</div>
</body>
</html>
```